Etiketten für Kürbiskernöl
Zielgruppe
Wir betreiben eine Landwirschaft, vorwiegend Ackerbau und Viehwirtschaft im nordöstlichen Niederösterreich. Wir sind ein reines Familienunternehmen. Unsere Zielgruppe ist 20 Jahre aufwärts, männlich wie weiblich und legt großen Wert auf Regionalität und hohe Qualität der Produkte.
Aufgabenstellung
Das Etikett wird für unsere Kürbiskernölflasche benötigt. Die Vorderseite soll unseren Namen, Produktbezeichnung und Füllmenge enthalten. Familie Wendtner - Kürbiskernöl 100% rein - 500ml Für die Rückseite gibt es einen entsprechenden Text (siehe Anhang).
Angehängt haben wir auch Etikett Vorderseiten, die uns sehr ansprechen. Es soll auf jeden Fall ein Kürbis abgebildet sein und ein hochwertiges, eher minimalistischen Design haben.
In Zukunft könnten wir uns auch vorstellen die Kürbiskerne in Form von Knabberkernen zu verkaufen, wofür wir das Etikettendesign gern abwandeln würden.
Farben: dunkelgrau/schwarz, weiß, dunkelgrün/oliv, beige
Flaschenform: Valmera 500ml siehe Foto

```html
<!DOCTYPE html>
<html lang="de">
<head>
<meta charset="utf-8">
<title>Kürbiskernöl – Rückenetikett</title>
<link href="https://fonts.googleapis.com/css2?family=Quicksand:wght@300;400&display=swap" rel="stylesheet">
<style>
  :root {
    --label-bg: #101210;
    --text-main: #ececec;
    --text-soft: #d6d6d6;
    --rule: #8a8a8a;
    --ornament-tone: #1b1d1b;
  }
  html, body {
    margin: 0;
    padding: 0;
    width: 1200px;
    height: 3130px;
    overflow: hidden;
    background: var(--label-bg);
  }
  .back-label {
    position: relative;
    width: 1200px;
    height: 3130px;
    background: var(--label-bg);
    font-family: "Quicksand", sans-serif;
    font-weight: 300;
    color: var(--text-main);
  }
  .product-story {
    position: absolute;
    top: 142px;
    right: 67px;
    margin: 0;
    text-align: right;
    font-size: 66px;
    line-height: 75px;
    white-space: nowrap;
    letter-spacing: 0.5px;
  }
  .divider {
    position: absolute;
    top: 1321px;
    left: 97px;
    width: 1037px;
    height: 0;
    border-top: 1.5px solid var(--rule);
  }
  .storage-note {
    position: absolute;
    top: 1366px;
    right: 94px;
    margin: 0;
    font-size: 48px;
    line-height: 60px;
    color: var(--text-soft);
    white-space: nowrap;
  }
  .vine-ornament {
    position: absolute;
    top: 1629px;
    left: 146px;
    width: 997px;
    height: 876px;
    background: radial-gradient(ellipse at 50% 55%, #222422 0%, var(--ornament-tone) 55%, var(--label-bg) 80%);
  }
  .producer {
    position: absolute;
    top: 2762px;
    right: 90px;
    margin: 0;
    text-align: right;
    font-size: 56px;
    line-height: 62px;
    font-style: normal;
    white-space: nowrap;
  }
  .best-before {
    position: absolute;
    top: 3008px;
    right: 67px;
    margin: 0;
    font-size: 54px;
    line-height: 64px;
    color: var(--text-soft);
    white-space: nowrap;
  }
</style>
</head>
<body>
  <main class="back-label">
    <p class="product-story">
      Nur die besten Kürbiskerne<br>
      aus unserem eigenen Anbau<br>
      werden zu unserem g'sund,<br>
      g'schmackig, guatem<br>
      Kürbiskernöl verarbeitet -<br>
      100% rein und naturbelassen.<br>
      Die Kürbiskerne werden<br>
      schonend geröstet und in<br>
      einem traditionellen Verfahren<br>
      in einer regionalen Ölmühle<br>
      kalt gepresst, was unserem<br>
      Kürbiskernöl das einzigartige,<br>
      intensiv-nussige Aroma<br>
      verleiht.
    </p>

    <div class="divider"></div>

    <p class="storage-note">Vor Wärme und Licht geschützt lagern</p>

    <div class="vine-ornament" role="img" aria-label="Feine Linienzeichnung von Kürbisblättern mit Ranken"></div>

    <address class="producer">
      Familie Wendtner<br>
      2071 Lindenbach 48
    </address>

    <p class="best-before">Mindestens haltbar bis: Oktober 2022</p>
  </main>
</body>
</html>
```